Book/Ebook Cover design for teen girls on purity/modesty
The Shape of Stillness: A Young Woman's Map to Quiet Strength
Book/Ebook Cover design for teen girls on purity/modesty - Books
Creative Brief
This book will be marketed to teenage girls, female family members like moms, grandmothers, aunts, etc., youth pastors, pastors, etc. I want a clean, fresh yet feminine look and feel. I envision an ornate mirror (handheld or otherwise) with the word "purity" being reflected on the mirror from the title. That is what's in my mind but I'm open to other ideas. Colors I like: aqua blue, bright green, and white.
Books
Feminine, fresh, charming, clean, modern.
This book will be published through Inkvale Press and Pagebrook. Full Bleed needed for the hard copy book. No less that 300 DPI. Need to know the basics about trim, margin, etc for book covers. RGB preferred.
tmerrow tmerrow
To Designers, I've uploaded an updated bio for myself for the back cover. I'll be choosing a winner very soon! Thank you so much for all your designs and hard work. I really appreciate it! Colette
FRIENDLY NOTE TO ALL DESIGNERS! Thanks for all your designs so far. Please do not include images of girls. I want the cover to draw girls from all backgrounds and an image of a girl whose skin color, hair and clothing makes a statement to one particular kind of girl. I want to make a statement to as many different kinds of girls as possible as the message is for them all. Also author name should either read "Colette J. Merrow" or "Colette Merrow". That's all for now. Please let me know how else I can help.
To all designers, Thanks for your willingness to create a design for my book! Size of book is 5.5X8.5. I'll need front and back cover designed. The mirror idea (described in the brief) is just something in my head. It can be pulled off believe but I'm also open to whatever fresh, clean and modern ideas you may have! Thanks again, tmerrow
Hi designers, It was brought to my attention that possibly the reason I haven't been getting many designers to commit is because this project isn't marked "guaranteed". I was under the impression that all projects were guaranteed. I do intend on picking a winner! I will call CS first thing Monday to see if I can change the project to read that it indeed is guaranteed. Until then, thanks so much for your submissions! I'm looking forward to picking one of your designs!
Dear designers, I would like to see some minimalistic designs. Simplistic but charming and feminine with a modern touch. Maybe the background the aqua blue color I like with a cute sketch of a mirror in white or with "purity" in a script font of some sort in the mirror. I'm not sure I'm going to like any of the random background kind of pictures. Thanks so much everyone. Tmerrow
Designers, The text for the back cover has not also been uploaded. Thanks!
To all designers, Thanks ahead of time for taking time to work on this project! I'm super excited to see what you all come up with. Please don't hesitate to ask questions or make suggestions. I have uploaded my head shot to use for the back cover. I am putting the finishing touches on the text for the back cover as well and will have that uploaded tonight or tomorrow. I'm not sure about how the ISBN will be printed on the book. Getting details on that as well. Thanks again! tmerrow

```html
<!DOCTYPE html>
<html lang="en">
<head>
<meta charset="utf-8">
<title>The Shape of Stillness – Book Cover</title>
<link href="https://fonts.googleapis.com/css2?family=Special+Elite&family=Tinos:wght@400&family=Arimo:wght@400&display=swap" rel="stylesheet">
<style>
  :root {
    --paper: #ffffff;
    --back-pink: #ea176c;
    --petal-light: #f7c9d6;
    --petal-mid: #f2a3bb;
    --petal-deep: #e77d9d;
    --title-pink: #e9628f;
    --title-shadow: rgba(255, 255, 255, 0.55);
    --ink: #111111;
    --label-white: #ffffff;
    --photo-dark: #3a2a2c;
    --photo-warm: #7a5a4c;
  }
  * { margin: 0; padding: 0; box-sizing: border-box; }
  html, body {
    width: 1200px;
    height: 874px;
    overflow: hidden;
    background: var(--paper);
  }
  .spread {
    position: relative;
    width: 1200px;
    height: 874px;
    background: var(--paper);
  }

  /* Front cover */
  .front-cover {
    position: absolute;
    left: 0;
    top: 0;
    width: 492px;
    height: 874px;
    overflow: hidden;
  }
  .front-cover .flower-photo {
    position: absolute;
    inset: 0;
    width: 100%;
    height: 100%;
  }
  .cover-title {
    position: absolute;
    left: 0;
    top: 205px;
    width: 100%;
    padding-left: 36px;
    text-align: center;
    font-family: "Special Elite", "Courier New", monospace;
    font-size: 66px;
    line-height: 84px;
    color: var(--title-pink);
    text-shadow: 0 0 6px var(--title-shadow);
    font-weight: 400;
  }
  .cover-title span { display: block; }

  /* Back cover */
  .back-cover {
    position: absolute;
    left: 595px;
    top: 0;
    width: 605px;
    height: 874px;
    background: var(--back-pink);
  }
  .author-photo {
    position: absolute;
    left: 41px;
    top: 22px;
    width: 158px;
    height: 160px;
  }
  .author-name {
    position: absolute;
    left: 41px;
    top: 184px;
    font-family: "Arimo", Arial, sans-serif;
    font-size: 17px;
    color: var(--label-white);
  }
  .back-copy {
    position: absolute;
    left: 20px;
    top: 224px;
    width: 574px;
    font-family: "Tinos", "Times New Roman", serif;
    font-size: 18.5px;
    line-height: 25.8px;
    color: var(--ink);
  }
  .back-copy .blurb {
    text-align: justify;
  }
  .back-copy .goals {
    margin-top: 26px;
    text-align: center;
    list-style: none;
  }
  .back-copy .goals-heading {
    text-align: center;
    margin-top: 22px;
  }
</style>
</head>
<body>
<main class="spread">

  <section class="front-cover">
    <svg class="flower-photo" role="img" aria-label="Close-up photograph of a soft pink daisy-like flower filling the cover" viewBox="0 0 492 874" preserveAspectRatio="none">
      <defs>
        <radialGradient id="petalGlow" cx="0.55" cy="0.95" r="1.05">
          <stop offset="0" stop-color="#f5b3c6"/>
          <stop offset="0.45" stop-color="#f7c9d6"/>
          <stop offset="0.8" stop-color="#f2a9bf"/>
          <stop offset="1" stop-color="#e88aa6"/>
        </radialGradient>
      </defs>
      <rect width="492" height="874" fill="url(#petalGlow)"/>
    </svg>
    <h1 class="cover-title">
      <span>A</span>
      <span>Young</span>
      <span>Woman's Map</span>
      <span>to</span>
      <span>Quiet</span>
      <span>Strength</span>
    </h1>
  </section>

  <section class="back-cover">
    <svg class="author-photo" role="img" aria-label="Author headshot photograph" viewBox="0 0 158 160" preserveAspectRatio="none">
      <defs>
        <linearGradient id="headshotTone" x1="0" y1="0" x2="0" y2="1">
          <stop offset="0" stop-color="#4a3a3a"/>
          <stop offset="1" stop-color="#2e2224"/>
        </linearGradient>
      </defs>
      <rect width="158" height="160" fill="url(#headshotTone)"/>
    </svg>
    <p class="author-name">Colette Merrow</p>

    <div class="back-copy">
      <p class="blurb">What does purity look like? Is it recognizable to the average teenage girl? Does she know that purity should be at the very foundation of her identity over makeup, short skirts, and finding a boyfriend? Purity carries an unpopular message in our culture, but the ignorance of purity could quite possibly be the greatest cause of the low self-esteem epidemic among teenage girls in our society. If a girl doesn't understand what kind of woman she was created to become, then chances are she will believe lies about herself from modern culture. As a result, throughout her life she will behave as if she's a much lesser being than her creator meant her to be. She may even become sexually active early in an attempt to feel desired and accepted. It's time she learns that her true beauty radiates brightly from the inside out!</p>
      <p class="goals-heading">The Shape of Stillness will:</p>
      <ul class="goals">
        <li>1. Define what purity is from God's perspective…not the world's.</li>
        <li>2. Teach teenage girls Biblically about their true identity and purpose amid the lies from media and pop culture.</li>
        <li>3. Guide teenage girls to sexual purity through a deeper walk with their creator.</li>
        <li>4. Help teenage girls overcome&nbsp; 5. Major obstacles to living a lifestyle of purity.</li>
      </ul>
    </div>
  </section>

</main>
</body>
</html>
```